Communication Business Card Design

We offer complete cabling solutions
Data Cabling,Fibre Optic, and Cabling Repairs fault finding
Security camera installation
TV Aerial installation
Security alarm installation
HWR

Industry/Entity Type

Business

Contact Information for Business Card

Brightmoor Solutions
ABN 58 214 992 367
EMAIL brightmoorsolutions.com.au
Mobile 0491236057
Lou Archer

```html
<!DOCTYPE html>
<html lang="en">
<head>
<meta charset="utf-8">
<title>Brightmoor Solutions — Business Card</title>
<link rel="stylesheet" href="https://fonts.googleapis.com/css2?family=Josefin+Sans:wght@400;600&family=Open+Sans:wght@400;600&display=swap">
<style>
  :root {
    --backdrop: #ecebe8;
    --card: #f4f4f4;
    --charcoal: #2c2c2c;
    --cyan: #12a8d0;
    --text-grey: #5a5a5a;
    --white: #ffffff;
  }
  * { box-sizing: border-box; margin: 0; padding: 0; }
  html, body {
    width: 1200px; height: 800px; overflow: hidden;
    background: var(--backdrop);
  }
  .canvas {
    width: 1200px; height: 800px;
    display: flex; align-items: center; justify-content: center; gap: 60px;
  }
  .card {
    width: 520px; height: 310px;
    background: var(--card);
    border-radius: 4px;
    box-shadow: 0 2px 10px rgba(0,0,0,0.12);
    position: relative; overflow: hidden;
  }

  /* Front */
  .card--front {
    display: flex; align-items: center; justify-content: center; gap: 22px;
    padding: 0 40px;
  }
  .brand-dot {
    flex: 0 0 auto;
    width: 40px; height: 40px; border-radius: 50%;
    background: var(--cyan);
  }
  .brand-name {
    font-family: "Josefin Sans", sans-serif;
    font-weight: 600;
    font-size: 30px;
    letter-spacing: 5px;
    text-transform: uppercase;
    color: var(--cyan);
    line-height: 1.2;
    white-space: nowrap;
    padding-top: 6px;
  }
  .brand-line { display: block; }

  /* Back */
  .card--back { display: flex; }
  .name-panel {
    flex: 0 0 200px; height: 100%;
    background: var(--charcoal);
    padding: 100px 0 0 40px;
    font-family: "Josefin Sans", sans-serif;
    font-size: 28px;
    letter-spacing: 1.5px;
    line-height: 1.15;
    text-transform: uppercase;
    white-space: nowrap;
  }
  .name-first { color: var(--white); display: block; }
  .name-last { color: var(--cyan); display: block; }
  .accent-band { flex: 0 0 16px; height: 100%; background: var(--cyan); }
  .details {
    flex: 1; padding: 86px 20px 0 16px;
    font-family: "Open Sans", sans-serif;
  }
  .abn-tag {
    background: var(--cyan); color: var(--white);
    font-size: 12px; font-weight: 600; letter-spacing: 0.5px;
    height: 22px; line-height: 22px; text-align: center;
    border-radius: 3px;
  }
  .contact-row {
    display: flex; align-items: center; gap: 12px;
    margin-top: 16px;
    font-size: 13px; color: var(--text-grey);
    white-space: nowrap;
  }
  .contact-row:first-of-type { margin-top: 18px; }
  .contact-icon {
    flex: 0 0 auto;
    width: 22px; height: 22px; border-radius: 50%;
    background: var(--cyan);
    display: flex; align-items: center; justify-content: center;
  }
</style>
</head>
<body>
<main class="canvas">
  <section class="card card--front" aria-label="Card front">
    <span class="brand-dot"></span>
    <h1 class="brand-name">
      <span class="brand-line">Brightmoor</span>
      <span class="brand-line">Solutions</span>
    </h1>
  </section>

  <section class="card card--back" aria-label="Card back">
    <div class="name-panel">
      <span class="name-first">Lou</span>
      <span class="name-last">Archer</span>
    </div>
    <div class="accent-band"></div>
    <div class="details">
      <p class="abn-tag">ABN 58 214 992 367</p>
      <p class="contact-row">
        <span class="contact-icon">
          <svg width="12" height="12" viewBox="0 0 24 24" aria-hidden="true">
            <path fill="#fff" d="M6.6 10.8a15.1 15.1 0 0 0 6.6 6.6l2.2-2.2a1 1 0 0 1 1-.25 11.4 11.4 0 0 0 3.6.57 1 1 0 0 1 1 1V20a1 1 0 0 1-1 1A17 17 0 0 1 3 4a1 1 0 0 1 1-1h3.5a1 1 0 0 1 1 1c0 1.250.2 2.450.57 3.57a1 1 0 0 1-.25 1z"/>
          </svg>
        </span>
        0491236057
      </p>
      <p class="contact-row">
        <span class="contact-icon">
          <svg width="12" height="12" viewBox="0 0 24 24" aria-hidden="true" fill="none" stroke="#fff" stroke-width="2">
            <circle cx="12" cy="12" r="9"/>
            <ellipse cx="12" cy="12" rx="4" ry="9"/>
            <line x1="3" y1="12" x2="21" y2="12"/>
          </svg>
        </span>
        brightmoorsolutions.com.au
      </p>
    </div>
  </section>
</main>
</body>
</html>
```